A corporate website

The target design is for Velmora Glassworks coporate site which is a major international manufacturers for the finest quality of transparent and colored full lead crystal (more than 30% PbO)

Velmora Glassworks is the largest producer of crystal in world with 98% of its production exported to more than 120 countries.

Velmora glassworks has 4 business lines:
1. Crystal Fashion Components
2. Chandeliers Crystal Parts
3. Lighting Collection and special design
4. Gifts and accessories

The winner bidder(s) would be asked to do more jobs

The corporate website is the official site that represents Velmora HQ in front of world and it includes the following pages:
1. Home page
2. Facilities:
a. Factories overview
b. Factories image and video gallery
c. Show rooms locator
d. Quality Control
3. Media Center with the following sub pages
a. Press releases (Previous and future press releases)
b. Logos & artwork (Hi res images for Velmora Glassworks to be used by various worldwide media)
c. Media contacts (contacts of Velmora’s media division)
4. Careers:
a. Publish opened positions from Pindle hire
b. Capture candidates resumes using Pindle hire form
5. About US
Updates

Target Market(s)

Business partners, resellers, end customers, press and employees

Industry/Entity Type

Business

Requirements
Must have
• The design should include a home webpage and an internal page design. The design should fullfill the following requriements:

1. Strictly follow the corporate identity materials guidelines - see attachment
2. Supports multi-language
3. User can change between languages using flags
4. Web surfer can optionally change the default language
5. An integrated live chat push button for ChatTrove
8. Site Header should contain the following information:
a. Logo
b. Slogan
c. Links to site pages
d. Link to the home page
e. Link to the landing page
f. A language option drop box
9. Footers should have:
a. Links to all other 5 websites in a dropbox form
b. Link to privacy statement
c. Link to copyright notice
d. Link to sitemap
e. Newsletter subscription one field form
11. Every sub-site should have a universal customer service section that offer the following services:
a. Links to end user installation manuals
b. Links to products cleaning and maintenance guide
c. Customer complaints center
12. A news sub-section that should contain:
a. Latest product and promotional announcements
b. Corporate news
c. Exhibitions coverage
13. A link to velmora Worldwide:
a. A database driven interactive map reflecting Velmora list of agents and distributors worldwide with list of supported products this interactive map could be limited in every sub-site for specific line of product
b. Capture potential resellers and agents
c. Become a partner form

```html
<!DOCTYPE html>
<html lang="en">
<head>
<meta charset="utf-8">
<title>Velmora Glassworks</title>
<link href="https://fonts.googleapis.com/css2?family=Arimo:wght@400;700&family=Dancing+Script:wght@600&display=swap" rel="stylesheet">
<style>
:root{
  --page:#cfdde8;
  --panel:#e6f0f7;
  --panel-line:#a9bfd0;
  --ink:#1e3a52;
  --muted:#8fa3b4;
  --link:#4f7fa6;
  --header-top:#3c4c5c;
  --header-bottom:#aebfcc;
  --footer-top:#8aa0b2;
  --footer-bottom:#6e8599;
  --orange:#ee7a1f;
  --orange-light:#f7a04f;
  --blue-tab:#6aa5d3;
  --teal-tab:#6fd0c0;
  --tan-tab:#d9a36c;
  --placeholder:#d3e2ed;
  --online:#e0661c;
}
*{box-sizing:border-box;margin:0;padding:0}
html,body{width:960px;height:1200px;overflow:hidden}
body{position:relative;background:var(--page);font-family:"Arimo",Arial,sans-serif;color:var(--ink)}
.abs{position:absolute}
.header-band{left:0;top:0;width:960px;height:173px;background:linear-gradient(180deg,var(--header-top) 0%,#6f8294 45%,var(--header-bottom) 100%)}
.brand{left:168px;top:19px;width:111px;height:78px;background:#fff;border-radius:6px;box-shadow:0 2px 4px rgba(0,0,0,.25);display:flex;flex-direction:column;align-items:center;justify-content:center;gap:6px}
.brand-mark{width:14px;height:14px;border-radius:50%;background:#9aa7b2}
.brand-name{font-size:14px;letter-spacing:1px;color:#5c6b78}
.lang{left:616px;top:17px;width:192px;height:22px;border-radius:11px;background:linear-gradient(#eef3f7,#c9d6e0);font-size:9px;color:#6f8090;display:flex;align-items:center;padding-left:14px;gap:8px;border:1px solid #fff}
.lang-flag{width:14px;height:9px;background:#3b5a99;border:1px solid #d33}
.lang-arrow{position:absolute;right:0;top:0;width:20px;height:20px;border-radius:50%;background:#5b90c8}
.nav{left:344px;top:67px;width:464px;height:29px;border-radius:5px;background:linear-gradient(#f7fafc,#d2dde6);box-shadow:0 1px 3px rgba(0,0,0,.2);display:flex;align-items:center;justify-content:space-around;font-size:10px}
.nav a{color:#4c6378;text-decoration:none}
.nav a.active{color:#2f6ea8}
.hero{left:104px;top:115px;width:751px;height:238px;border-radius:6px;background:radial-gradient(ellipse at 45% 50%,#b9c8d6 0%,#6d7f90 30%,#1d2731 65%,#0c1117 100%);border:1px solid #fff}
.hero-card{left:616px;top:133px;width:176px;height:194px;border-radius:6px;background:#f4f8fb;padding:16px 14px}
.hero-card h2{font-size:12.5px;line-height:20px;color:var(--ink);letter-spacing:.3px}
.hero-card p{font-size:10.5px;line-height:15px;color:var(--muted);margin-top:5px}
.btn-orange{display:block;margin:14px auto 0;width:112px;height:28px;border-radius:5px;background:linear-gradient(var(--orange-light),var(--orange));color:#fff;font-family:"Dancing Script",cursive;font-size:16px;text-align:center;line-height:28px}
.hero-rule{left:104px;top:363px;width:751px;height:9px;border-radius:4px;background:#dfe9f1}
.panel{background:var(--panel);border:1px solid var(--panel-line);border-radius:6px}
.panel-title{position:absolute;left:13px;top:8px;font-family:"Dancing Script",cursive;font-size:21px;color:#2b4862}
.placeholder{background:var(--placeholder);border:1px solid #fff;border-radius:4px;color:#8a9bab;font-size:8px;display:flex;align-items:center;justify-content:center}
.news-item h3{font-size:12.5px;font-weight:400;color:var(--ink)}
.news-item p{font-size:10.5px;line-height:15px;color:var(--muted);margin-top:6px}
.tab-label{position:absolute;width:239px;text-align:center;color:#fff}
.tab-label strong{display:block;font-weight:400;font-size:16.5px;letter-spacing:.5px}
.tab-label span{display:block;font-size:8px;margin-top:1px}
.world h2{font-size:17px;font-weight:400;color:var(--ink)}
.world p{font-size:10.5px;line-height:17.5px;color:var(--muted)}
.map{background:linear-gradient(135deg,#e7e4dc,#d7d6cf 60%,#cfd8c6);border:4px solid #fff;box-shadow:0 1px 3px rgba(0,0,0,.2)}
.help-bubble{left:627px;top:711px;width:218px;height:47px;background:#fff;border:1px solid var(--panel-line);border-radius:8px;font-size:20px;color:#7c8c99;padding:11px 0 0 26px}
.agent-photo{background:linear-gradient(#e6ecf1,#b3c2cf);border:4px solid #fff;outline:1px solid #9fb3c4}
.agent h3{font-size:12px;font-weight:700;color:var(--ink)}
.agent p{font-size:10px;line-height:15px;color:var(--link)}
.agent .status-off{color:#b5c3ce}
.agent .status-on{color:var(--online);font-weight:700}
.footer{left:0;top:1037px;width:960px;height:163px;background:linear-gradient(var(--footer-top),var(--footer-bottom))}
.footer-links{font-size:12px;color:#fff}
.footer-text{font-size:9.5px;line-height:20px;color:#b4c3cf}
.newsletter{left:616px;top:1056px;width:239px;height:124px;border-radius:7px;background:#6b8093}
</style>
</head>
<body>

<div class="abs header-band"></div>

<div class="abs brand"><div class="brand-mark"></div><div class="brand-name">VELMORA</div></div>

<div class="abs lang"><span class="lang-flag"></span>- English ( Great Britain ) -<span class="lang-arrow"></span></div>

<nav class="abs nav">
  <a class="active" href="#">Home</a><a href="#">Facilities</a><a href="#">Media Center</a><a href="#">Contact Us</a><a href="#">Careers</a><a href="#">About Us</a>
</nav>

<div class="abs hero" role="img" aria-label="Close-up photograph of a faceted pear-shape crystal chandelier bead"></div>
<div class="abs hero-card">
  <h2>Pear-Shape<br>Crystal Chandelier Bead</h2>
  <p>Vivamus sagittis lacus vel augue laoreet rutrum faucibus dolor auctor. Aenean lacinia bibendum nulla sed consectetur. Praesent com-</p>
  <a class="btn-orange">Action Button</a>
</div>
<div class="abs hero-rule"></div>

<!-- recent product -->
<section class="abs panel" style="left:104px;top:385px;width:239px;height:230px">
  <div class="panel-title">The Most Recent Product</div>
  <div class="abs" role="img" aria-label="Photograph of a cut crystal gem" style="left:31px;top:46px;width:177px;height:88px;background:linear-gradient(#e4eef5,#c9d9e5);border-radius:6px 6px 0 0"></div>
  <div class="abs" style="left:0;top:134px;width:237px;height:1px;background:var(--panel-line)"></div>
  <div class="abs" style="left:17px;top:152px;font-size:12.5px">The Crystal</div>
</section>

<!-- latest news -->
<section class="abs panel" style="left:360px;top:385px;width:239px;height:230px">
  <div class="panel-title">Latest News</div>
  <div class="abs placeholder" style="left:15px;top:46px;width:80px;height:78px">Image</div>
  <div class="abs news-item" style="left:111px;top:54px;width:120px"><h3>Justo Odio</h3><p>Lorem ipsum dolor sit amet, consectetur adipiscing elit. Vesti-</p></div>
  <div class="abs placeholder" style="left:15px;top:134px;width:80px;height:77px">Image</div>
  <div class="abs news-item" style="left:111px;top:142px;width:120px"><h3>Egestas Eget</h3><p>Nullam quis risus eget urna mollis ornare vel eu leo.</p></div>
</section>

<!-- exhibition -->
<section class="abs panel" style="left:616px;top:385px;width:239px;height:230px">
  <div class="panel-title">Exhibition</div>
  <div class="abs placeholder" style="left:31px;top:46px;width:176px;height:145px">Image</div>
  <div class="abs" style="left:0;top:199px;width:237px;text-align:center;font-size:12.5px;color:var(--muted)">Exhibition Caption</div>
</section>

<!-- service tabs -->
<svg class="abs" style="left:104px;top:633px" width="751" height="48" viewBox="0 0 751 48">
  <polygon points="10,0 229,0 239,24 229,48 10,48 0,24" fill="var(--blue-tab)"/>
  <polygon points="266,0 485,0 495,24 485,48 266,48 256,24" fill="var(--teal-tab)"/>
  <polygon points="522,0 741,0 751,24 741,48 522,48 512,24" fill="var(--tan-tab)"/>
</svg>
<div class="tab-label" style="left:104px;top:643px"><strong>Installation Manual</strong><span>Browse Our Documented Product's manual</span></div>
<div class="tab-label" style="left:360px;top:643px"><strong>Maintenance Guide</strong><span>All the maintenance you need to know</span></div>
<div class="tab-label" style="left:616px;top:643px"><strong>Customer Center</strong><span>Need help ?, Please visit our Trained Staff</span></div>

<!-- worldwide -->
<section class="abs panel world" style="left:104px;top:701px;width:495px;height:315px">
  <h2 class="abs" style="left:15px;top:12px">Velmora Worldwide</h2>
  <p class="abs" style="left:15px;top:35px;width:162px">Vivamus sagittis lacus vel augue laoreet rutrum faucibus dolor auctor. Cras mattis consectetur purus sit amet fermentum. Aenean lacinia bibendum nulla sed consectetur.</p>
  <p class="abs" style="left:15px;top:168px;width:162px">Donec id elit non mi porta gravida at eget metus. Nullam quis risus eget urna mollis ornare vel eu leo. Maecenas faucibus mollis interdum. Maecenas sed diam eget risus varius blandit sit</p>
  <div class="abs" style="left:118px;top:288px;font-size:9px;color:var(--ink)">Read More &gt;&gt;</div>
  <div class="abs map" role="img" aria-label="Street map marking the Velmora Glassworks headquarters" style="left:192px;top:18px;width:283px;height:164px"></div>
  <div class="abs" style="left:192px;top:190px;font-size:12.5px;font-weight:700;color:var(--ink)">Velmora Glassworks</div>
  <div class="abs" style="left:192px;top:212px;font-size:10px;color:var(--muted)">5, Velmora glassworks St., Harrowgate Quarter, Lindmere</div>
  <svg class="abs" style="left:192px;top:248px" width="283" height="30" viewBox="0 0 283 30">
    <polygon points="0,0 131,0 140,15 131,30 0,30" fill="#8ea3b5"/>
    <polygon points="131,0 283,0 274,15 283,30 131,30 140,15" fill="#5fa0d6"/>
  </svg>
  <div class="abs" style="left:192px;top:257px;width:131px;text-align:center;font-size:10.5px;color:#fff">Want to join us ?</div>
  <div class="abs" style="left:330px;top:257px;width:145px;text-align:center;font-size:10.5px;color:#fff">Become Our Partner</div>
</section>

<!-- live help -->
<section class="abs panel" style="left:616px;top:701px;width:239px;height:315px"></section>
<div class="abs help-bubble">Need Help ?</div>
<svg class="abs" style="left:790px;top:756px" width="20" height="14" viewBox="0 0 20 14"><polygon points="0,0 16,0 18,14" fill="#fff" stroke="var(--panel-line)"/></svg>
<div class="abs" style="left:616px;top:777px;width:239px;text-align:center;font-size:12px;color:#4f6a80">Chat With Us Live!</div>

<div class="abs agent-photo" role="img" aria-label="Portrait of support agent Tobin wearing a headset" style="left:656px;top:805px;width:77px;height:78px"></div>
<div class="abs agent" style="left:743px;top:813px"><h3>Tobin</h3><p style="margin-top:4px">Premium<br>Support<br><span class="status-off">Offline</span></p></div>
<div class="abs agent-photo" role="img" aria-label="Portrait of crystal specialist Maren wearing a headset" style="left:656px;top:901px;width:77px;height:78px"></div>
<div class="abs agent" style="left:743px;top:909px"><h3>Maren</h3><p style="margin-top:4px">Crystal<br>Specialist<br><span class="status-on">Online</span></p></div>
<svg class="abs" style="left:799px;top:835px" width="14" height="140" viewBox="0 0 14 140">
  <g fill="none" stroke="#b9c7d2" stroke-width="1.2">
    <circle cx="7" cy="5" r="4"/><rect x="2" y="18" width="10" height="7"/><polyline points="2,18 7,22 12,18"/>
    <circle cx="7" cy="101" r="4"/><rect x="2" y="114" width="10" height="7"/><polyline points="2,114 7,118 12,114"/>
  </g>
</svg>
<div class="abs" style="left:616px;top:998px;width:239px;text-align:center;font-size:9.5px;color:#b0c0cc">Powered by chattrove API</div>

<!-- footer -->
<footer class="abs footer"></footer>
<div class="abs footer-links" style="left:104px;top:1062px">Home | Facilities | Media Center | Contact Us | Careers | About Us</div>
<p class="abs footer-text" style="left:104px;top:1089px;width:440px">Praesent commodo cursus magna, vel scelerisque nisl consectetur et. Duis mollis, est non commodo luctus, nisi erat porttitor ligula, eget lacinia odio sem nec elit. Aenean eu leo</p>
<div class="abs" style="left:104px;top:1170px;font-size:10px;color:#fff">Privacy Statement | Sitemap | Term of Use</div>

<div class="abs newsletter">
  <svg class="abs" style="left:45px;top:10px" width="18" height="18" viewBox="0 0 18 18"><rect width="18" height="18" rx="3" fill="var(--orange)"/><circle cx="5" cy="13" r="2" fill="#fff"/><path d="M4 8a6 6 0 0 1 6 6M4 4a10 10 0 0 1 10 10" stroke="#fff" stroke-width="2" fill="none"/></svg>
  <div class="abs" style="left:76px;top:15px;font-size:10px;font-weight:700;color:#fff">Subscribe to our newsletter</div>
  <div class="abs" style="left:32px;top:37px;width:178px;height:21px;border-radius:10px;background:#4d6072;font-size:10px;color:#c5d2dc;text-align:center;line-height:21px">Enter your email here</div>
  <div class="abs" style="left:32px;top:74px;font-size:8px;color:#b4c3cf">We never share your privacy</div>
  <div class="abs" style="left:153px;top:67px;width:56px;height:20px;border-radius:8px;background:linear-gradient(var(--orange-light),var(--orange));font-size:10px;font-weight:700;color:#fff;text-align:center;line-height:20px">Enter</div>
</div>

</body>
</html>
```